Brightmark Pixel Collective Website

I need my website redesigned to look very modern with the latest services. Check out my old website for information: www.brightmarkpixelcollective.com

You can use the same site menu links

It doesn't need to have the Recent News section

Please use the yellow, black and grey color scheme

Target Market(s)

25-50 years in range. Small Business Owners

Industry/Entity Type

Group

Requirements
Must have
• Logo and similar color scheme to current website
• Modern, Modern, Modern! I want a very fresh and modern look
Should not have
• Boring Look

```html
<!DOCTYPE html>
<html lang="en">
<head>
<meta charset="utf-8">
<title>Brightmark Pixel Collective</title>
<link href="https://fonts.googleapis.com/css2?family=Open+Sans:wght@300;400;600;700&display=swap" rel="stylesheet">
<style>
:root{
  --yellow:#fdb913;
  --yellow-dark:#e9a500;
  --black:#111111;
  --dark:#1c1c1c;
  --card:#161616;
  --grey:#8a8a8a;
  --white:#ffffff;
  --text:#222222;
}
*{margin:0;padding:0;box-sizing:border-box}
html,body{width:753px;height:1200px;overflow:hidden}
body{font-family:"Open Sans",Arial,sans-serif;background:var(--white);color:var(--text);position:relative}

.hero{position:absolute;left:0;top:0;width:753px;height:557px;
  background:radial-gradient(ellipse at 60% 35%,#3a3a3a 0%,#222 45%,#0d0d0d 100%)}
.hero-edge{position:absolute;left:0;top:552px;width:753px;height:6px;background:var(--yellow)}
.hero-notch{position:absolute;left:356px;top:556px;width:0;height:0;
  border-left:20px solid transparent;border-right:20px solid transparent;border-top:18px solid var(--yellow)}

.main-nav{position:absolute;top:12px;left:151px;display:flex;gap:10px}
.nav-item{width:84px;height:82px;background:var(--yellow);display:flex;flex-direction:column;
  align-items:center;justify-content:center;gap:8px;font-size:11px;color:var(--black);font-weight:600}
.nav-item svg{width:24px;height:24px;fill:var(--black)}

.brand{position:absolute;top:232px;left:0;width:753px;text-align:center}
.brand-mark{width:60px;height:60px;background:var(--yellow);margin:0 auto 40px}
.brand-name{font-size:26px;font-weight:300;letter-spacing:2px;color:#d9d9d9;text-transform:uppercase}

.estimate-btn{position:absolute;left:296px;top:472px;width:165px;height:44px;background:var(--yellow);
  display:flex;align-items:center;justify-content:center;gap:10px;font-size:11px;font-weight:600;color:var(--black)}
.estimate-btn svg{width:18px;height:18px;fill:var(--black)}

.about{position:absolute;top:574px;left:0;width:753px;text-align:center}
.about-icon{width:52px;height:52px;border-radius:50%;background:var(--yellow);margin:48px auto 0;
  display:flex;align-items:center;justify-content:center}
.about-icon svg{width:26px;height:26px;fill:var(--black)}
.about-title{font-size:24px;font-weight:700;color:var(--black);margin-top:12px;letter-spacing:.5px}
.about-tag{display:inline-block;background:var(--yellow);color:var(--white);font-size:10px;
  padding:6px 24px;margin-top:8px;width:217px}

.team{position:absolute;top:798px;left:0;width:753px;height:369px;background:var(--yellow)}
.team-notch{position:absolute;left:356px;top:0;width:0;height:0;
  border-left:20px solid transparent;border-right:20px solid transparent;border-top:18px solid var(--white)}
.team-intro{position:absolute;top:36px;left:100px;width:558px;font-size:9.5px;line-height:15px;color:var(--black)}
.team-grid{position:absolute;top:138px;left:100px;display:flex;gap:28px}
.member{width:118px;height:200px;background:var(--card);text-align:center}
.member-photo{height:100px;background:linear-gradient(180deg,#f2f2f2 0%,#bdbdbd 100%)}
.member-name{color:var(--white);font-size:10px;margin-top:14px}
.member-role{color:var(--white);font-size:8px;margin-top:6px}
.member-links{display:flex;justify-content:center;gap:5px;margin-top:12px}
.member-links span{width:16px;height:16px;border-radius:50%;background:var(--yellow)}

.footer{position:absolute;top:1167px;left:0;width:753px;height:33px;background:var(--black)}
.footer-notch{position:absolute;left:354px;top:0;width:0;height:0;
  border-left:22px solid transparent;border-right:22px solid transparent;border-top:22px solid var(--yellow)}
</style>
</head>
<body>

<header class="hero" role="img" aria-label="Dark photo of a business desk with printed charts">
  <nav class="main-nav">
    <div class="nav-item"><svg viewBox="0 0 24 24"><path d="M12 3 2 12h3v9h5v-6h4v6h5v-9h3z"/></svg>Home</div>
    <div class="nav-item"><svg viewBox="0 0 24 24"><circle cx="12" cy="7" r="5"/><path d="M3 22c0-5 4-8 9-8s9 3 9 8z"/></svg>About us</div>
    <div class="nav-item"><svg viewBox="0 0 24 24"><path d="M9 4h6v3h6v13H3V7h6zm2 2v1h2V6z"/></svg>Services</div>
    <div class="nav-item"><svg viewBox="0 0 24 24"><path d="M3 7h4l2-3h6l2 3h4v13H3z"/><circle cx="12" cy="13" r="4" fill="#fdb913"/><circle cx="12" cy="13" r="2.2"/></svg>Portfolio</div>
    <div class="nav-item"><svg viewBox="0 0 24 24"><path d="M16 3l5 5-12 12H4v-5z"/></svg>Contact us</div>
  </nav>
</header>

<div class="brand">
  <div class="brand-mark"></div>
  <div class="brand-name">Brightmark Pixel Collective</div>
</div>

<div class="estimate-btn">
  <svg viewBox="0 0 24 24"><path d="M3 5h10v2H5v12h12v-8h2v10H3z"/><path d="M18 2l4 4-9 9H9v-4z"/></svg>
  Request a Free Estimate
</div>

<div class="hero-edge"></div>
<div class="hero-notch"></div>

<section class="about">
  <div class="about-icon"><svg viewBox="0 0 24 24"><circle cx="12" cy="7" r="5"/><path d="M3 22c0-5 4-8 9-8s9 3 9 8z"/></svg></div>
  <h2 class="about-title">ABOUT</h2>
  <div class="about-tag">Lorem Ipsum is simply dummy text of the</div>
</section>

<section class="team">
  <div class="team-notch"></div>
  <p class="team-intro">Contrary to popular belief, Lorem Ipsum is not simply random text. It has roots in a piece of classical Latin literature from 45 BC, making it over 2000 years old. Henry Aldous, a Latin professor at Brookfield College in Vermont, looked up one of the more obscure Latin words, consectetur, from a Lorem Ipsum passage, and going through the cites of the word in classical literature, discovered the undoubtable source. Lorem Ipsum comes from sections 1.10.32 and 1.10.</p>
  <div class="team-grid">
    <div class="member">
      <div class="member-photo" role="img" aria-label="Portrait photo of the CEO"></div>
      <div class="member-name">Lena Ortiz</div>
      <div class="member-role">CEO</div>
      <div class="member-links"><span></span><span></span><span></span></div>
    </div>
    <div class="member">
      <div class="member-photo" role="img" aria-label="Portrait photo of the web designer"></div>
      <div class="member-name">Owen</div>
      <div class="member-role">Web Designer</div>
      <div class="member-links"><span></span><span></span><span></span></div>
    </div>
    <div class="member">
      <div class="member-photo" role="img" aria-label="Portrait photo of the online marketing expert"></div>
      <div class="member-name">Ravi Anand</div>
      <div class="member-role">Online Marketing Expert</div>
      <div class="member-links"><span></span><span></span><span></span></div>
    </div>
    <div class="member">
      <div class="member-photo" role="img" aria-label="Portrait photo of the graphic designer"></div>
      <div class="member-name">Tomas</div>
      <div class="member-role">Graphic Designer</div>
      <div class="member-links"><span></span><span></span><span></span></div>
    </div>
  </div>
</section>

<footer class="footer"><div class="footer-notch"></div></footer>

</body>
</html>
```